MS Word Template needed for a company specialized in Insurance and Finance Advising

I am looking for an impressive and memorable Word Template for:

Writing daily letters
Presentations
Agreements
Front Pages for Projects
Finance, pension, tax analyzes ...

Our logo is attached.
We are advising clients in all kind of questions in the finance and insurance industry, we are not selling products, our main business is the advising and to win the trust to all kind of costumers, from young to old from all kind of nations.

```html
<!DOCTYPE html>
<html lang="en">
<head>
<meta charset="utf-8">
<title>Ridgeway Advisory – Document Template Set</title>
<link href="https://fonts.googleapis.com/css2?family=Oswald:wght@400;500&family=Montserrat:wght@400;600;700&family=Roboto:wght@400&display=swap" rel="stylesheet">
<style>
:root{
  --red:#e30613;
  --red-dark:#c4000b;
  --grey-bg:#d3d3d3;
  --grey-band:#9b9b9e;
  --grey-light:#c9c9cb;
  --ink:#333;
  --ink-soft:#555;
  --white:#fff;
}
*{margin:0;padding:0;box-sizing:border-box}
html,body{width:854px;height:1200px;overflow:hidden;background:var(--grey-bg)}
body{position:relative;font-family:"Montserrat",sans-serif;color:var(--ink)}
.page{position:absolute;width:242px;height:348px;background:var(--white);overflow:hidden;box-shadow:1px 1px 3px rgba(0,0,0,.25)}
.label{position:absolute;width:242px;text-align:center;font-family:"Roboto",sans-serif;font-size:17px;color:#333;letter-spacing:.3px}
.page-header{position:absolute;left:0;top:0;width:242px;height:24px}
.page-header svg{display:block}
.header-title{position:absolute;left:7px;top:4px;font-family:"Oswald",sans-serif;font-size:10px;color:var(--white)}
.brand-mark{position:absolute;right:5px;top:7px;font-family:"Montserrat",sans-serif;font-weight:700;font-size:7.5px;color:var(--red);letter-spacing:.2px}
.page-footer{position:absolute;left:0;bottom:0;width:242px;height:11px}
.footer-copy{position:absolute;left:5px;bottom:2px;font-size:3.6px;color:var(--white)}
.footer-num{position:absolute;right:12px;bottom:2px;font-size:4.2px;color:#555}
.p{font-size:4px;line-height:6.2px;color:var(--ink-soft)}
.abs{position:absolute}
.h-red{font-weight:600;color:var(--red)}
.placeholder-circle{position:absolute;width:62px;height:62px;border-radius:50%;background:#d0d0d0;border:2px solid #fff;box-shadow:0 0 0 1.5px #bdbdbd;display:flex;align-items:center;justify-content:center;text-align:center;font-size:7.5px;line-height:9px;color:#444}
.toc-title{position:absolute;left:22px;top:54px;font-size:8px;color:#333}
.toc-row{position:absolute;left:22px;width:200px;display:flex;align-items:flex-end;font-size:4px;color:#444}
.toc-row .dots{flex:1;border-bottom:.5px solid #999;margin:0 3px 1px}
.tbl-title{position:absolute;left:9px;font-size:6px;font-weight:600;color:#222}
table.data{position:absolute;left:9px;width:224px;border-collapse:collapse;font-size:3.6px;color:#444}
table.data th{font-weight:600;text-align:left;padding:1.5px 3px}
table.data td{padding:1.6px 3px}
.style-1 thead th{border-top:.8px solid #222;border-bottom:.5px solid #999}
.style-1 tbody tr:last-child td{border-bottom:.5px solid #999}
.style-2 thead th{background:#d6d6d6}
.style-3{outline:.8px solid var(--red)}
.style-3 thead th{background:var(--red);color:#fff}
</style>
</head>
<body>

<!-- Cover page -->
<section class="page cover" style="left:22px;top:22px">
  <svg width="242" height="348" viewBox="0 0 242 348" class="abs" style="left:0;top:0">
    <defs>
      <linearGradient id="coverRed" x1="0" y1="0" x2="1" y2="1">
        <stop offset="0" stop-color="#d8000f"/>
        <stop offset="1" stop-color="#b8000a"/>
      </linearGradient>
    </defs>
    <path d="M0 0H242V118C205 150 150 205 60 232C35 240 15 243 0 244Z" fill="#9e9ea0" transform="translate(0,6)"/>
    <path d="M0 0H242V118C205 150 150 205 60 232C35 240 15 243 0 244Z" fill="url(#coverRed)" role="img" aria-label="Office meeting photograph with red overlay"/>
    <rect x="0" y="337" width="242" height="11" fill="var(--grey-band)"/>
  </svg>
  <div class="abs" style="left:0;width:190px;top:100px;text-align:center;font-family:'Oswald',sans-serif;font-size:18px;color:#fff;font-weight:500">PROJECT TITLE HERE</div>
  <div class="abs" style="left:0;width:190px;top:124px;text-align:center;font-family:'Oswald',sans-serif;font-size:9px;color:#fff">SUBTEXT HERE</div>
  <div class="abs" style="left:0;width:242px;top:274px;text-align:center;font-weight:700;font-size:17px;color:var(--red)">RIDGEWAY</div>
</section>
<div class="label" style="left:22px;top:373px">COVER PAGE</div>

<!-- Page 01: Contents -->
<section class="page" style="left:306px;top:22px">
  <header class="page-header">
    <svg width="242" height="24" viewBox="0 0 242 24"><rect width="242" height="24" fill="var(--red)"/><path d="M160 24C178 20 192 8 206 0H242V24Z" fill="#fff"/><path d="M164 24C182 18 196 6 210 0" stroke="#b0b0b0" stroke-width="1" fill="none"/></svg>
    <span class="header-title">Project Heading Here</span><span class="brand-mark">RIDGEWAY</span>
  </header>
  <div class="toc-title">Table Content</div>
  <div class="toc-row" style="top:76px"><span>Table of Content</span><span class="dots"></span><span>01</span></div>
  <div class="toc-row" style="top:93px"><span>About US</span><span class="dots"></span><span>01</span></div>
  <div class="toc-row" style="top:110px"><span>Out Graphs</span><span class="dots"></span><span>01</span></div>
  <div class="toc-row" style="top:127px"><span>Table of Content</span><span class="dots"></span><span>01</span></div>
  <div class="toc-row" style="top:144px"><span>Table of Content</span><span class="dots"></span><span>01</span></div>
  <div class="toc-row" style="top:161px"><span>Table of Content</span><span class="dots"></span><span>01</span></div>
  <div class="toc-row" style="top:178px"><span>Table of Content</span><span class="dots"></span><span>01</span></div>
  <div class="toc-row" style="top:195px"><span>Table of Content</span><span class="dots"></span><span>01</span></div>
  <div class="toc-row" style="top:212px"><span>Table of Content</span><span class="dots"></span><span>01</span></div>
  <div class="toc-row" style="top:229px"><span>Table of Content</span><span class="dots"></span><span>01</span></div>
  <div class="toc-row" style="top:246px"><span>Table of Content</span><span class="dots"></span><span>01</span></div>
  <div class="toc-row" style="top:263px"><span>Table of Content</span><span class="dots"></span><span>01</span></div>
  <div class="toc-row" style="top:280px"><span>Table of Content</span><span class="dots"></span><span>01</span></div>
  <footer class="page-footer"><svg width="242" height="11" viewBox="0 0 242 11"><path d="M0 3H195C205 3 210 11 222 11H0Z" fill="var(--grey-band)"/><path d="M195 3H242V11H222C210 11 205 3 195 3Z" fill="#e6e6e6"/></svg><span class="footer-copy">Copyright text here</span><span class="footer-num">01</span></footer>
</section>
<div class="label" style="left:306px;top:373px">PAGE - 01</div>

<!-- Page 02: Headings & text -->
<section class="page" style="left:586px;top:22px">
  <header class="page-header">
    <svg width="242" height="24" viewBox="0 0 242 24"><rect width="242" height="24" fill="var(--red)"/><path d="M160 24C178 20 192 8 206 0H242V24Z" fill="#fff"/><path d="M164 24C182 18 196 6 210 0" stroke="#b0b0b0" stroke-width="1" fill="none"/></svg>
    <span class="header-title">Project Heading Here</span><span class="brand-mark">RIDGEWAY</span>
  </header>
  <div class="abs h-red" style="left:20px;top:46px;font-size:10.5px">Main Heading Here 1</div>
  <div class="abs" style="left:20px;top:67px;font-size:9px;color:#999;font-weight:600">Main Heading Here 2</div>
  <div class="abs" style="left:20px;top:88px;font-size:7.5px;color:#333;font-weight:600">Main Heading Here 3</div>
  <div class="abs p" style="left:20px;top:111px;width:206px">
    <p>Lorem ipsum dolor sit amet, consectetur adipiscing elit, sed do eiusmod tempor incididunt ut labore et dolore magna aliqua. Ut enim ad minim veniam, quis nostrud exercitation ullamco laboris nisi ut aliquip ex ea commodo consequat. Duis aute irure dolor in reprehenderit in voluptate velit esse</p>
    <p style="margin-top:5px">Cillum dolore eu fugiat nulla pariatur. Excepteur sint occaecat cupidatat non proident, sunt in culpa qui officia deserunt mollit anim id est laborum.”</p>
    <p style="margin-top:5px">“Sed ut perspiciatis unde omnis iste natus error sit voluptatem accusantium doloremque laudantium, totam rem aperiam, eaque ipsa quae ab illo inventore veritatis et quasi architecto beatae vitae dicta sunt explicabo. Nemo enim ipsam voluptatem quia voluptas sit aspernatur aut odit aut fugit, sed quia consequuntur magni dolores eos qui ratione voluptatem sequi nesciunt. Neque porro quisquam est, qui dolorem ipsum quia dolor sit amet, consectetur, adipisci velit, sed quia non numquam eius modi tempora incidunt ut labore et dolore magnam aliquam quaerat voluptatem. Ut enim ad minima veniam, quis nostrum exercitationem ullam corporis suscipit laboriosam, nisi ut aliquid ex ea commodi consequatur? Quis autem vel eum iure reprehenderit qui in ea voluptate velit esse quam nihil molestiae consequatur, vel illum qui dolorem eum fugiat quo voluptas nulla pariatur?”Lorem ipsum dolor sit amet, consectetur adipiscing elit, sed do eiusmod tempor incididunt ut labore et dolore magna aliqua.</p>
    <p style="margin-top:5px">Ut enim ad minim veniam, quis nostrud exercitation ullamco laboris nisi ut aliquip ex ea commodo consequat. Duis aute irure dolor in reprehenderit in voluptate velit esse cillum dolore eu fugiat nulla pariatur. Excepteur sint occaecat cupidatat non proident, sunt in culpa qui officia deserunt mollit anim id est laborum.”</p>
  </div>
  <footer class="page-footer"><svg width="242" height="11" viewBox="0 0 242 11"><path d="M0 3H195C205 3 210 11 222 11H0Z" fill="var(--grey-band)"/><path d="M195 3H242V11H222C210 11 205 3 195 3Z" fill="#e6e6e6"/></svg><span class="footer-copy">Copyright text here</span><span class="footer-num">01</span></footer>
</section>
<div class="label" style="left:586px;top:373px">PAGE - 02</div>

<!-- Page 03: Image + text -->
<section class="page" style="left:22px;top:410px">
  <header class="page-header">
    <svg width="242" height="24" viewBox="0 0 242 24"><rect width="242" height="24" fill="var(--red)"/><path d="M160 24C178 20 192 8 206 0H242V24Z" fill="#fff"/><path d="M164 24C182 18 196 6 210 0" stroke="#b0b0b0" stroke-width="1" fill="none"/></svg>
    <span class="header-title">Project Heading Here</span><span class="brand-mark">RIDGEWAY</span>
  </header>
  <div class="placeholder-circle" style="left:15px;top:46px">IMAGE<br>HERE</div>
  <div class="placeholder-circle" style="left:15px;top:174px">IMAGE<br>HERE</div>
  <div class="abs h-red" style="left:86px;top:44px;font-size:8px">Main Heading Here 1</div>
  <div class="abs p" style="left:86px;top:55px;width:144px;text-align:justify">
    <p>Lorem ipsum dolor sit amet, consectetur adipiscing elit, sed do eiusmod tempor incididunt ut labore et dolore magna aliqua. Ut enim ad minim veniam, quis nostrud exercitation ullamco laboris nisi ut aliquip ex ea commodo consequat. Duis aute irure dolor in reprehenderit in voluptate velit esse</p>
    <p style="margin-top:5px">Cillum dolore eu fugiat nulla pariatur. Excepteur sint occaecat cupidatat non proident, sunt in culpa qui officia deserunt mollit anim id est laborum.”</p>
    <p style="margin-top:5px">Cillum dolore eu fugiat nulla pariatur. Excepteur sint occaecat cupidatat non proident, sunt in culpa qui officia deserunt mollit anim id est laborum.”</p>
  </div>
  <div class="abs h-red" style="left:86px;top:175px;font-size:8px">Main Heading Here 1</div>
  <div class="abs p" style="left:86px;top:186px;width:144px;text-align:justify">
    <p>“Sed ut perspiciatis unde omnis iste natus error sit voluptatem accusantium doloremque laudantium, totam rem aperiam, eaque ipsa quae ab illo inventore veritatis et quasi architecto beatae vitae dicta sunt explicabo. Nemo enim ipsam voluptatem quia voluptas sit aspernatur aut odit aut fugit, sed quia consequuntur magni dolores eos qui ratione voluptatem sequi nesciunt.</p>
    <p style="margin-top:5px">Neque porro quisquam est, qui dolorem ipsum quia dolor sit amet, consectetur, adipisci velit, sed quia non numquam eius modi tempora incidunt ut labore et dolore magnam aliquam quaerat voluptatem. Ut enim ad minima veniam, quis nostrum exercitationem ullam corporis suscipit laboriosam, nisi ut aliquid ex ea commodi consequatur? Quis autem vel eum iure reprehenderit qui in ea voluptate velit esse quam nihil molestiae consequatur, vel illum qui dolorem eum fugiat quo voluptas nulla pariatur?</p>
  </div>
  <footer class="page-footer"><svg width="242" height="11" viewBox="0 0 242 11"><path d="M0 3H195C205 3 210 11 222 11H0Z" fill="var(--grey-band)"/><path d="M195 3H242V11H222C210 11 205 3 195 3Z" fill="#e6e6e6"/></svg><span class="footer-copy">Copyright text here</span><span class="footer-num">01</span></footer>
</section>
<div class="label" style="left:22px;top:762px">PAGE - 03</div>

<!-- Page 04: Two columns -->
<section class="page" style="left:306px;top:410px">
  <header class="page-header">
    <svg width="242" height="24" viewBox="0 0 242 24"><rect width="242" height="24" fill="var(--red)"/><path d="M160 24C178 20 192 8 206 0H242V24Z" fill="#fff"/><path d="M164 24C182 18 196 6 210 0" stroke="#b0b0b0" stroke-width="1" fill="none"/></svg>
    <span class="header-title">Project Heading Here</span><span class="brand-mark">RIDGEWAY</span>
  </header>
  <div class="placeholder-circle" style="left:28px;top:61px">IMAGE<br>HERE</div>
  <div class="placeholder-circle" style="left:159px;top:61px">IMAGE<br>HERE</div>
  <div class="abs h-red" style="left:10px;width:106px;top:135px;font-size:8px;text-align:center">Main Heading Here 1</div>
  <div class="abs h-red" style="left:127px;width:106px;top:135px;font-size:8px;text-align:center">Main Heading Here 1</div>
  <div class="abs p" style="left:14px;top:146px;width:100px;text-align:center">
    <p>Lorem ipsum dolor sit amet, consectetur adipiscing elit, sed do eiusmod tempor incididunt ut labore et dolore magna aliqua. Ut enim ad minim veniam, quis nostrud exercitation ullamco laboris nisi ut aliquip ex ea commodo consequat. Duis aute irure dolor in reprehenderit in voluptate velit esse</p>
    <p style="margin-top:6px">Cillum dolore eu fugiat nulla pariatur. Excepteur sint occaecat cupidatat non proident, sunt in culpa qui officia deserunt mollit anim id est laborum.”</p>
    <p style="margin-top:6px">Cillum dolore eu fugiat nulla pariatur. Excepteur sint occaecat cupidatat non proident, sunt in culpa qui officia deserunt mollit anim id est laborum.”</p>
  </div>
  <div class="abs p" style="left:131px;top:146px;width:100px;text-align:center">
    <p>Lorem ipsum dolor sit amet, consectetur adipiscing elit, sed do eiusmod tempor incididunt ut labore et dolore magna aliqua. Ut enim ad minim veniam, quis nostrud exercitation ullamco laboris nisi ut aliquip ex ea commodo consequat. Duis aute irure dolor in reprehenderit in voluptate velit esse</p>
    <p style="margin-top:6px">Cillum dolore eu fugiat nulla pariatur. Excepteur sint occaecat cupidatat non proident, sunt in culpa qui officia deserunt mollit anim id est laborum.”</p>
    <p style="margin-top:6px">Cillum dolore eu fugiat nulla pariatur. Excepteur sint occaecat cupidatat non proident, sunt in culpa qui officia deserunt mollit anim id est laborum.”</p>
  </div>
  <footer class="page-footer"><svg width="242" height="11" viewBox="0 0 242 11"><path d="M0 3H195C205 3 210 11 222 11H0Z" fill="var(--grey-band)"/><path d="M195 3H242V11H222C210 11 205 3 195 3Z" fill="#e6e6e6"/></svg><span class="footer-copy">Copyright text here</span><span class="footer-num">01</span></footer>
</section>
<div class="label" style="left:306px;top:762px">PAGE - 04</div>

<!-- Page 05: Tables -->
<section class="page" style="left:586px;top:410px">
  <header class="page-header">
    <svg width="242" height="24" viewBox="0 0 242 24"><rect width="242" height="24" fill="var(--red)"/><path d="M160 24C178 20 192 8 206 0H242V24Z" fill="#fff"/><path d="M164 24C182 18 196 6 210 0" stroke="#b0b0b0" stroke-width="1" fill="none"/></svg>
    <span class="header-title">Project Heading Here</span><span class="brand-mark">RIDGEWAY</span>
  </header>
  <div class="abs p" style="left:9px;top:40px;width:224px">Lorem ipsum dolor sit amet, consectetur adipiscing elit, sed do eiusmod tempor incididunt ut labore et dolore magna aliqua. Ut enim ad minim veniam, quis nostrud exercitation ullamco laboris nisi ut aliquip ex ea commodo consequat. Duis aute irure dolor in reprehenderit in voluptate velit esse cillum dolore eu fugiat nulla pariatur. Excepteur sint occaecat cupidatat non proident, sunt in culpa qui officia deserunt mollit anim id est laborum.</div>
  <div class="tbl-title" style="top:90px">Table Style 1</div>
  <table class="data style-1" style="top:101px">
    <thead><tr><th>Title 1</th><th>Title 2</th><th>Title 3</th><th>Title 4</th><th>Title 5</th><th>Title 6</th></tr></thead>
    <tbody>
      <tr><td>Lorem ipsum dolor</td><td>xxx</td><td>xxx</td><td>xxx</td><td>xxx</td><td>xxx</td></tr>
      <tr><td>Lorem ipsum dolor</td><td>xxx</td><td>xxx</td><td>xxx</td><td>xxx</td><td>xxx</td></tr>
      <tr><td>Lorem ipsum dolor</td><td>xxx</td><td>xxx</td><td>xxx</td><td>xxx</td><td>xxx</td></tr>
      <tr><td>Lorem ipsum dolor</td><td>xxx</td><td>xxx</td><td>xxx</td><td>xxx</td><td>xxx</td></tr>
    </tbody>
  </table>
  <div class="tbl-title" style="top:167px;font-weight:400">Table Style 2</div>
  <table class="data style-2" style="top:178px">
    <thead><tr><th>Title 1</th><th>Title 2</th><th>Title 3</th><th>Title 4</th><th>Title 5</th><th>Title 6</th></tr></thead>
    <tbody>
      <tr><td>Lorem ipsum dolor</td><td>xxx</td><td>xxx</td><td>xxx</td><td>xxx</td><td>xxx</td></tr>
      <tr><td>Lorem ipsum dolor</td><td>xxx</td><td>xxx</td><td>xxx</td><td>xxx</td><td>xxx</td></tr>
      <tr><td>Lorem ipsum dolor</td><td>xxx</td><td>xxx</td><td>xxx</td><td>xxx</td><td>xxx</td></tr>
      <tr><td>Lorem ipsum dolor</td><td>xxx</td><td>xxx</td><td>xxx</td><td>xxx</td><td>xxx</td></tr>
    </tbody>
  </table>
  <div class="tbl-title" style="top:243px;color:var(--red)">Table Style 3</div>
  <table class="data style-3" style="top:254px">
    <thead><tr><th>Title 1</th><th>Title 2</th><th>Title 3</th><th>Title 4</th><th>Title 5</th><th>Title 6</th></tr></thead>
    <tbody>
      <tr><td>Lorem ipsum dolor</td><td>xxx</td><td>xxx</td><td>xxx</td><td>xxx</td><td>xxx</td></tr>
      <tr><td>Lorem ipsum dolor</td><td>xxx</td><td>xxx</td><td>xxx</td><td>xxx</td><td>xxx</td></tr>
      <tr><td>Lorem ipsum dolor</td><td>xxx</td><td>xxx</td><td>xxx</td><td>xxx</td><td>xxx</td></tr>
      <tr><td>Lorem ipsum dolor</td><td>xxx</td><td>xxx</td><td>xxx</td><td>xxx</td><td>xxx</td></tr>
    </tbody>
  </table>
  <footer class="page-footer"><svg width="242" height="11" viewBox="0 0 242 11"><path d="M0 3H195C205 3 210 11 222 11H0Z" fill="var(--grey-band)"/><path d="M195 3H242V11H222C210 11 205 3 195 3Z" fill="#e6e6e6"/></svg><span class="footer-copy">Copyright text here</span><span class="footer-num">01</span></footer>
</section>
<div class="label" style="left:586px;top:762px">PAGE - 05</div>

<!-- Page 06: Charts -->
<section class="page" style="left:186px;top:802px">
  <header class="page-header">
    <svg width="242" height="24" viewBox="0 0 242 24"><rect width="242" height="24" fill="var(--red)"/><path d="M160 24C178 20 192 8 206 0H242V24Z" fill="#fff"/><path d="M164 24C182 18 196 6 210 0" stroke="#b0b0b0" stroke-width="1" fill="none"/></svg>
    <span class="header-title">Project Heading Here</span><span class="brand-mark">RIDGEWAY</span>
  </header>
  <div class="abs h-red" style="left:9px;top:35px;font-size:5.5px;font-weight:700">Lorem ipsum dolor sit amet</div>
  <div class="abs p" style="left:9px;top:44px;width:224px">Lorem ipsum dolor sit amet, consectetur adipiscing elit, sed do eiusmod tempor incididunt ut labore et dolore magna aliqua. Ut enim ad minim veniam, quis nostrud exercitation ullamco laboris nisi ut aliquip ex ea commodo consequat. Duis aute irure dolor in reprehenderit in voluptate velit esse cillum dolore eu fugiat nulla pariatur. Excepteur sint occaecat cupidatat non proident, sunt in culpa qui officia deserunt mollit anim id est laborum.</div>
  <div class="abs" style="left:9px;top:92px;font-size:5.5px;font-weight:700;color:#222">Lorem ipsum dolor sit amet</div>
  <div class="abs p" style="left:9px;top:101px;width:224px">Lorem ipsum dolor sit amet, consectetur adipiscing elit, sed do eiusmod tempor incididunt ut labore et dolore magna aliqua. Ut enim ad minim veniam sed do eiusmod tempor</div>
  <svg class="abs" style="left:0;top:120px" width="242" height="66" viewBox="0 0 242 66" role="img" aria-label="Bar chart with three groups of bars">
    <rect x="24" y="30" width="16" height="30" fill="var(--red)"/>
    <rect x="46" y="21" width="16" height="39" fill="var(--red)"/>
    <rect x="68" y="36" width="16" height="24" fill="var(--red)"/>
    <rect x="104" y="36" width="14" height="24" fill="#8e8e90"/>
    <rect x="122" y="21" width="14" height="39" fill="#8e8e90"/>
    <rect x="140" y="49" width="14" height="11" fill="#8e8e90"/>
    <rect x="168" y="30" width="14" height="30" fill="#d6d6d6"/>
    <rect x="185" y="9" width="14" height="51" fill="#d6d6d6"/>
    <rect x="202" y="53" width="14" height="7" fill="#d6d6d6"/>
  </svg>
  <div class="abs p" style="left:9px;top:198px;width:224px">Lorem ipsum dolor sit amet, consectetur adipiscing elit, sed do eiusmod tempor incididunt ut labore et dolore magna aliqua. Ut enim ad minim veniam sed do eiusmod tempor</div>
  <svg class="abs" style="left:40px;top:220px" width="160" height="98" viewBox="0 0 160 98" role="img" aria-label="Line chart with five data series">
    <g stroke="#ddd" stroke-width=".4">
      <line x1="8" y1="10" x2="154" y2="10"/><line x1="8" y1="26" x2="154" y2="26"/><line x1="8" y1="42" x2="154" y2="42"/><line x1="8" y1="58" x2="154" y2="58"/><line x1="8" y1="74" x2="154" y2="74"/>
      <line x1="26" y1="4" x2="26" y2="90"/><line x1="44" y1="4" x2="44" y2="90"/><line x1="62" y1="4" x2="62" y2="90"/><line x1="80" y1="4" x2="80" y2="90"/><line x1="98" y1="4" x2="98" y2="90"/><line x1="116" y1="4" x2="116" y2="90"/><line x1="134" y1="4" x2="134" y2="90"/>
    </g>
    <line x1="8" y1="90" x2="154" y2="90" stroke="#999" stroke-width=".6"/>
    <line x1="8" y1="4" x2="8" y2="90" stroke="#999" stroke-width=".6"/>
    <g fill="none" stroke-width="1">
      <path d="M8 90C25 40 45 30 70 26S100 18 115 24S135 40 143 40" stroke="var(--red)"/>
      <path d="M8 90C30 50 45 40 70 38S100 30 115 36S135 24 143 20" stroke="#f05a28"/>
      <path d="M8 90C30 60 50 50 70 46S100 52 115 46S135 40 143 34" stroke="#bbb"/>
      <path d="M8 90C30 70 50 60 70 56S100 62 115 56S135 50 143 50" stroke="#999"/>
      <path d="M8 90C30 80 45 66 70 70S95 86 110 70S130 20 143 8" stroke="#555"/>
    </g>
    <g fill="#555"><circle cx="70" cy="70" r="1.5"/><circle cx="143" cy="8" r="1.5"/><circle cx="70" cy="56" r="1.5"/><circle cx="143" cy="50" r="1.5"/></g>
    <g fill="var(--red)"><circle cx="8" cy="90" r="1.5"/><circle cx="70" cy="26" r="1.5"/><circle cx="115" cy="24" r="1.5"/><circle cx="143" cy="40" r="1.5"/></g>
  </svg>
  <footer class="page-footer"><svg width="242" height="11" viewBox="0 0 242 11"><path d="M0 3H195C205 3 210 11 222 11H0Z" fill="var(--grey-band)"/><path d="M195 3H242V11H222C210 11 205 3 195 3Z" fill="#e6e6e6"/></svg><span class="footer-copy">Copyright text here</span><span class="footer-num">01</span></footer>
</section>
<div class="label" style="left:186px;top:1158px">PAGE - 06</div>

<!-- Back page -->
<section class="page" style="left:470px;top:802px">
  <div class="abs" style="left:0;top:0;width:242px;height:225px;background:var(--red)"></div>
  <div class="abs" style="left:0;width:242px;top:101px;text-align:center;font-family:'Oswald',sans-serif;font-size:10px;color:#fff">THANKS YOU VERY MUCH</div>
  <div class="abs" style="left:0;width:242px;top:129px;text-align:center;font-size:7px;color:#fff">Ridgeway Advisory</div>
  <div class="abs" style="left:0;width:242px;top:140px;text-align:center;font-size:4px;line-height:9.5px;color:#fff;font-weight:600">Office Address -1<br>Office Address -2<br>Office Address -3</div>
  <div class="abs" style="left:0;width:242px;top:270px;text-align:center;font-weight:700;font-size:17px;color:var(--red)">RIDGEWAY</div>
  <footer class="page-footer"><svg width="242" height="11" viewBox="0 0 242 11"><path d="M0 3H195C205 3 210 11 222 11H0Z" fill="var(--grey-band)"/><path d="M195 3H242V11H222C210 11 205 3 195 3Z" fill="#e6e6e6"/></svg><span class="footer-copy">Copyright text here</span><span class="footer-num">01</span></footer>
</section>
<div class="label" style="left:470px;top:1158px">BACK PAGE</div>

</body>
</html>
```